BRYLTAllies.co.uk - Mental Health Clinic for Child and Adolescents

Updated 29/01/2018***
I am not sure you guys are getting the idea regards to the opening page / homescreen layout. Can you look at the new images I have uploaded (page 5, 6 and 7) These are some of the layouts I like but to incorporate my chosen images, with the BRYLT commissioner, buttons and a sliding header bar.
I have written a strong brief, I am looking for a website, preferably wordpress as i know they are easy to maintain. I am looking for a one page site, with the top / opening page being full screen image with drop down categories. I have made a rough design, see full brief in word doc attached, there is some freedom to play around with the design aspect but it will need to relay all the content provided. I like a minimal feel. I have also attached some images that may be useful, but will need a new logo for BRYLT Allies. I have attached some logo idea's, it is up to you decide whether you want to use them.
I would prefer the homepage as full screen image, and the categories offered as a drop down or over the main image.
I have also attached linked to some competitors websites:
https://www.verdano-group.co.uk/
http://www.qwmr.org.uk/
Industry/Entity Type
Clinic
Number of Pages Required
1 page
Font styles to use
Look and feel
Each slider illustrates characteristics of the customer's brand and the style your logo design should communicate.

```html
<!DOCTYPE html>
<html lang="en">
<head>
<meta charset="utf-8">
<title>BRYLT Allies – Where Young Minds Matter</title>
<link href="https://fonts.googleapis.com/css2?family=Work+Sans:wght@500;600;700&family=Lato:wght@400;700&display=swap" rel="stylesheet">
<style>
:root{
  --teal:#1fbfa5;
  --purple:#5b1f6e;
  --band-blue:#3399ff;
  --heading-blue:#5b7fc0;
  --sidebar:rgba(12,12,12,.92);
  --text:#444;
  --muted:#555;
  --grey-bg:#f2f2f2;
  --white:#fff;
}
*{margin:0;padding:0;box-sizing:border-box}
html,body{width:709px;height:1200px;overflow:hidden;background:var(--white)}
body{font-family:"Lato",sans-serif;color:var(--text)}
.page{position:relative;width:709px;height:1200px;overflow:hidden}
.abs{position:absolute}

/* Hero */
.hero{left:0;top:0;width:709px;height:368px}
.hero-photo{left:0;top:0;width:709px;height:368px;
  background:linear-gradient(115deg,#8c7466 0%,#b7a79a 30%,#d9d2cb 55%,#c9b8a6 75%,#9c8a78 100%)}
.sidebar{left:0;top:0;width:106px;height:368px;background:var(--sidebar)}
.side-brand{position:absolute;left:0;top:14px;width:106px;text-align:center;color:var(--white)}
.side-brand .name{font-family:"Work Sans",sans-serif;font-weight:700;font-size:17px;letter-spacing:1px}
.side-brand .tag{font-family:"Work Sans",sans-serif;font-weight:600;font-size:5px;margin-top:2px}
.side-nav{position:absolute;left:0;top:68px;width:106px;list-style:none}
.side-nav li{height:37.6px;line-height:37.6px;text-align:center;border-bottom:1px dashed #555;
  font-family:"Work Sans",sans-serif;font-weight:600;font-size:8.5px;color:var(--white)}
.side-nav li:last-child{border-bottom:none}
.side-nav li:first-child{border-top:none}
.hero-brand{left:106px;width:603px;top:112px;text-align:center;color:var(--white);
  font-family:"Work Sans",sans-serif;font-weight:700;font-size:50px;letter-spacing:3px;line-height:1}
.hero-tag{left:106px;width:496px;top:186px;text-align:center;color:var(--white);
  font-family:"Work Sans",sans-serif;font-weight:600;font-size:19px}
.btn{display:block;text-align:center;border-radius:16px;color:var(--white);
  font-family:"Work Sans",sans-serif;font-weight:600}
.btn-parents{left:235px;top:230px;width:111px;height:32px;line-height:32px;font-size:11px;background:var(--teal)}
.btn-commissioners{left:362px;top:230px;width:112px;height:32px;line-height:32px;font-size:11px;background:var(--purple)}
.dots{left:336px;top:342px;display:flex;gap:4px}
.dots span{width:6px;height:6px;border-radius:50%;background:var(--white)}
.dots span.active{background:var(--teal)}

/* Announcement band */
.band{left:0;top:368px;width:709px;height:58px;background:var(--band-blue)}
.band-text{left:0;width:709px;top:20px;text-align:center;color:var(--white);
  font-family:"Work Sans",sans-serif;font-weight:600;font-size:12.5px;letter-spacing:.2px}
.band-arrow{top:22px}

/* Welcome */
.welcome{left:0;top:426px;width:709px;height:313px;
  background:linear-gradient(180deg,#fff 0%,#fff 38%,#e9e9e9 70%,#dcdcdc 100%)}
.welcome h1{position:absolute;left:0;width:709px;top:30px;text-align:center;
  font-family:"Work Sans",sans-serif;font-weight:600;font-size:21px;color:var(--heading-blue)}
.welcome p{position:absolute;left:46px;width:618px;top:65px;text-align:center;
  font-size:8.4px;line-height:15.5px;color:var(--muted)}
.btn-read{left:302px;top:123px;width:106px;height:32px;line-height:32px;font-size:10px;background:var(--teal)}
.group-photo{left:0;top:134px;width:709px;height:179px;
  background:linear-gradient(180deg,rgba(255,255,255,0) 0%,rgba(196,170,150,.55) 30%,#9a7f6e 65%,#5e7f80 100%)}

/* Blog */
.blog{left:0;top:739px;width:709px;height:311px;background:var(--grey-bg)}
.blog h2{position:absolute;left:0;width:709px;top:26px;text-align:center;
  font-family:"Work Sans",sans-serif;font-weight:600;font-size:18px;color:var(--heading-blue)}
.post{top:67px;width:195px}
.post-image{width:195px;height:108px}
.post-title{margin-top:13px;font-family:"Work Sans",sans-serif;font-weight:600;font-size:11.6px;
  line-height:16px;color:var(--purple)}
.post-excerpt{margin-top:2px;font-size:8.3px;line-height:13.6px;color:var(--muted)}
.post-link{margin-top:6px;font-size:8.5px;font-weight:700;color:var(--teal)}

/* Footer */
.footer{left:0;top:1050px;width:709px;height:150px;background:var(--white)}
.foot-brand{left:56px;top:28px;font-family:"Work Sans",sans-serif;font-weight:700;font-size:27px;
  letter-spacing:1.5px;color:var(--teal);line-height:1}
.foot-tag{left:44px;top:62px;font-family:"Work Sans",sans-serif;font-weight:600;font-size:9px;color:var(--purple)}
.copyright{left:44px;top:88px;font-size:7.4px;line-height:13px;color:var(--muted)}
.foot-head{font-family:"Lato",sans-serif;font-weight:700;font-size:9px;color:var(--teal);letter-spacing:.3px}
.foot-list{list-style:none;font-size:7.8px;line-height:17px;color:var(--muted)}
.foot-text{font-size:7.8px;line-height:13px;color:var(--muted)}
.contact-row{display:flex;align-items:center;gap:12px;font-size:7.8px;color:var(--muted)}
.social{display:flex;gap:10px}
.social span{width:12px;height:12px;border-radius:50%;background:#222}
</style>
</head>
<body>
<div class="page">

  <header class="hero abs">
    <div class="hero-photo abs" role="img" aria-label="Photo of a counsellor with a clipboard talking with a young person in a bright room"></div>
    <nav class="sidebar abs">
      <div class="side-brand">
        <div class="name">BRYLT</div>
        <div class="tag">Where Young Minds Matter</div>
      </div>
      <ul class="side-nav">
        <li>About Us</li><li>Our Team</li><li>Our Services</li><li>Contact Us</li>
        <li>Parents</li><li>Commissioners</li><li>Blog</li><li>Forum</li>
      </ul>
    </nav>
    <div class="hero-brand abs">BRYLT</div>
    <div class="hero-tag abs" style="left:160px">Where Young Minds Matter</div>
    <a class="btn btn-parents abs">Parents</a>
    <a class="btn btn-commissioners abs">Commissioners</a>
    <div class="dots abs"><span class="active"></span><span></span><span></span><span></span></div>
  </header>

  <section class="band abs">
    <svg class="band-arrow abs" style="left:180px" width="8" height="12" viewBox="0 0 8 12"><path d="M6.5 1 1.5 6l5 5" fill="none" stroke="#fff" stroke-width="2"/></svg>
    <div class="band-text abs">ADHD and ASD screening within 24 hours..</div>
    <svg class="band-arrow abs" style="left:522px" width="8" height="12" viewBox="0 0 8 12"><path d="M1.5 1l5 5-5 5" fill="none" stroke="#fff" stroke-width="2"/></svg>
  </section>

  <section class="welcome abs">
    <div class="group-photo abs" role="img" aria-label="Photo of five smiling young people sitting together on a sofa in front of a white brick wall"></div>
    <h1>Welcome to Our Website</h1>
    <p>Aliquam molestie, mi et imperdiet euismod, dui purus auctor tellus, et &nbsp;interdum lacus lectus et ante. Sed accumsan sollicitudin sapien, sit amet adipiscing turpis gravida ac. In congue, neque ac lobortis volutpat, libero mauris varius mi, vitae suscipit ipsum ligula vitae risus. Duis aliquam nibh a dui iaculis viverra id a velit. Vivamus egestas risus in magna varius &nbsp;commodo.</p>
    <a class="btn btn-read abs">Read More</a>
  </section>

  <section class="blog abs">
    <h2>Blog Posts</h2>
    <article class="post abs" style="left:44px">
      <div class="post-image" role="img" aria-label="Photo of a teenage boy talking with a counsellor at a desk" style="background:linear-gradient(135deg,#6f6a66,#b9b2aa 60%,#8a7f78)"></div>
      <h3 class="post-title">Aliquam molestie mi et imperdiet euismod aliquam</h3>
      <p class="post-excerpt">Interdum lacus lectus et ante. Sed accumsan sollicitudin sapien, sit amet adipiscing turpis gravida ac primis in faucibus..</p>
      <div class="post-link">Continue Reading</div>
    </article>
    <article class="post abs" style="left:256px">
      <div class="post-image" role="img" aria-label="Photo of a therapist with a clipboard and a young girl on a sofa" style="background:linear-gradient(135deg,#d8d2c8,#8aa0c0 50%,#c9b8a2)"></div>
      <h3 class="post-title">Aliquam molestie mi et imperdiet euismod aliquam</h3>
      <p class="post-excerpt">Interdum lacus lectus et ante. Sed accumsan sollicitudin sapien, sit amet adipiscing turpis gravida ac primis in faucibus..</p>
      <div class="post-link">Continue Reading</div>
    </article>
    <article class="post abs" style="left:469px">
      <div class="post-image" role="img" aria-label="Photo of a girl listening to a counsellor in a home setting" style="background:linear-gradient(135deg,#e7e2dc,#b08f7e 55%,#d8c7b8)"></div>
      <h3 class="post-title">Aliquam molestie mi et imperdiet euismod aliquam</h3>
      <p class="post-excerpt">Interdum lacus lectus et ante. Sed accumsan sollicitudin sapien, sit amet adipiscing turpis gravida ac primis in faucibus..</p>
      <div class="post-link">Continue Reading</div>
    </article>
  </section>

  <footer class="footer abs">
    <div class="foot-brand abs">BRYLT</div>
    <div class="foot-tag abs">Where Young Minds Matter</div>
    <div class="copyright abs">Copyright © 2018. Company Name<br>All Right Reserved</div>

    <div class="abs" style="left:202px;top:29px">
      <div class="foot-head">QUICK LINKS</div>
    </div>
    <ul class="foot-list abs" style="left:202px;top:43px">
      <li>Home</li><li>About us</li><li>Our Team</li><li>Our Services</li><li>Contact Us</li>
    </ul>
    <ul class="foot-list abs" style="left:281px;top:43px">
      <li>Parents</li><li>Commissioners</li><li>Blog</li><li>Forum</li>
    </ul>

    <div class="foot-head abs" style="left:362px;top:29px">CONTACT INFO</div>
    <div class="foot-text abs" style="left:362px;top:46px">Larkfield Suite 2B, 41-47 Mill Lane,<br>London, E14 7RT</div>
    <div class="contact-row abs" style="left:362px;top:77px">
      <svg width="8" height="8" viewBox="0 0 24 24"><path d="M6.6 10.8a15 15 0 0 0 6.6 6.6l2.2-2.2c.3-.3.7-.4 1-.2 1.1.4 2.3.6 3.6.6.6 0 1 .4 1 1V20c0 .6-.4 1-1 1A17 17 0 0 1 3 4c0-.6.4-1 1-1h3.5c.6 0 1 .4 1 1 0 1.3.2 2.5.6 3.6.1.3 0 .7-.2 1z" fill="#333"/></svg>
      <span>0203 555 0187</span>
    </div>
    <div class="contact-row abs" style="left:362px;top:95px">
      <svg width="8" height="7" viewBox="0 0 24 18"><path d="M0 0h24v18H0z" fill="#333"/><path d="M1 1l11 9 11-9" fill="none" stroke="#fff" stroke-width="2"/></svg>
      <span>enquiry@bryltallies.co.uk</span>
    </div>

    <div class="foot-head abs" style="left:530px;top:29px">OPENING TIMES</div>
    <div class="foot-text abs" style="left:530px;top:46px">Mon- Fri &nbsp;&nbsp;9am - 5pm</div>
    <div class="foot-head abs" style="left:530px;top:73px">FOLLOW US</div>
    <div class="social abs" style="left:530px;top:92px" aria-label="Social media links">
      <span></span><span></span><span></span><span></span><span></span><span></span>
    </div>
  </footer>

</div>
</body>
</html>
```